Nail Technician Business Card Design

My business is a nail technician business which involves applying nail enhancements to clients nails. I would like a design that uses the colours:, purple or black and silver on a light grey background. The final design should entice clients to my business.
I would like appointment times on the back of the card.
I want the spilled bottle on the front and the other one on the back
I would like the dragonfly font
Updates
Project Deadline Extended
Reason: I have found a font I would like used and also an image/logo
I have listed some ideas I would like used on the design of my card. thanks
Tessa
Industry/Entity Type
Business
Contact Information for Business Card
Lumen Nail Designs
41 Wendover street,
Yarrowee, NSW 2791
Mobile: 0400 582 316
Tessa Harcourt
Like us on Linkbook
Font styles to use
Other font styles liked:
- Dragonfly
Look and feel
Each slider illustrates characteristics of the customer's brand and the style your logo design should communicate.

```html
<!DOCTYPE html>
<html lang="en">
<head>
<meta charset="utf-8">
<title>Lumen Nail Designs – Business Card</title>
<link rel="stylesheet" href="https://fonts.googleapis.com/css2?family=Mystery+Quest&family=IM+Fell+English:ital@1&display=swap">
<style>
  :root {
    --page: #ffffff;
    --card-black: #050505;
    --panel-black: #0c0b0d;
    --purple: #8a2f9c;
    --purple-deep: #5b1a6e;
    --purple-light: #b06cc4;
    --lavender: #c58fd6;
    --silver: #dcdce2;
    --skin: #e6b9a6;
  }
  * { margin: 0; padding: 0; box-sizing: border-box; }
  html, body {
    width: 1200px;
    height: 960px;
    overflow: hidden;
    background: var(--page);
  }
  .sheet {
    position: relative;
    width: 1200px;
    height: 960px;
  }
  .card {
    position: absolute;
    left: 240px;
    width: 720px;
    height: 420px;
    overflow: hidden;
    box-shadow: 0 6px 18px rgba(0, 0, 0, 0.18);
  }

  /* Brand side */
  .card--brand {
    top: 40px;
    background: var(--card-black);
  }
  .brand-art {
    position: absolute;
    left: 130px;
    top: 0;
    width: 590px;
    height: 210px;
    background:
      radial-gradient(ellipse 34% 45% at 30% 72%, #7a2a86 0%, #4d1457 60%, transparent 100%),
      radial-gradient(ellipse 40% 55% at 82% 30%, #a56cbc 0%, #6d3a80 55%, transparent 100%);
  }
  .brand-name {
    position: absolute;
    left: 150px;
    top: 118px;
    font-family: "Mystery Quest", cursive;
    font-size: 40px;
    color: var(--silver);
    letter-spacing: 1px;
  }

  /* Contact side */
  .card--contact {
    top: 500px;
    background: linear-gradient(135deg, var(--purple-light) 0%, var(--purple) 45%, var(--purple-deep) 100%);
  }
  .contact-panel {
    position: absolute;
    left: 54px;
    top: 50px;
    width: 620px;
    height: 330px;
    overflow: hidden;
    background: var(--panel-black);
  }
  .hand-photo {
    position: absolute;
    right: 0;
    top: 30px;
    width: 90px;
    height: 150px;
    background: linear-gradient(160deg, var(--skin) 0%, #c98a93 40%, var(--purple) 70%, var(--purple-deep) 100%);
  }
  .contact-name {
    position: absolute;
    left: 0;
    width: 530px;
    top: 40px;
    text-align: center;
    font-family: "Mystery Quest", cursive;
    font-size: 60px;
    font-weight: 400;
    color: var(--purple);
    white-space: nowrap;
  }
  .contact-address {
    position: absolute;
    left: 18px;
    top: 188px;
    font-family: "IM Fell English", serif;
    font-style: italic;
    font-size: 26px;
    color: var(--lavender);
    white-space: nowrap;
  }
  .contact-mobile {
    position: absolute;
    right: 20px;
    top: 234px;
    font-family: "IM Fell English", serif;
    font-style: italic;
    font-size: 26px;
    color: var(--lavender);
    white-space: nowrap;
  }
  .contact-social {
    position: absolute;
    right: 20px;
    top: 278px;
    font-family: "Mystery Quest", cursive;
    font-size: 30px;
    color: var(--purple);
    white-space: nowrap;
  }
</style>
</head>
<body>
<main class="sheet">
  <section class="card card--brand" aria-label="Card front">
    <div class="brand-art" role="img" aria-label="Spilled purple nail polish bottle with glitter splash"></div>
    <p class="brand-name">lumen nail designs</p>
  </section>

  <section class="card card--contact" aria-label="Card back">
    <div class="contact-panel">
      <div class="hand-photo" role="img" aria-label="Hand with glitter purple painted nails"></div>
      <h1 class="contact-name">tessa harcourt</h1>
      <p class="contact-address">41 Wendover street, Yarrowee NSW 2791</p>
      <p class="contact-mobile">Mobile: 0400 582 316</p>
      <p class="contact-social">like us on linkbook</p>
    </div>
  </section>
</main>
</body>
</html>
```